New Zealand Marlborough Sauvignon Blanc wine packaging design

We need packaging design for our new wine brand, Dunmore Hale. The wine is a New Zealand Marlborough Sauvignon Blanc. We would like the packaging will portray elegance and style with an understated label. We are looking for a label that portrays the elegance of the French Riviera. The label should be round or pill shaped.
Updates

Industry/Entity Type

Wine

Font styles to use
Serif
Sans Serif

Requirements
Must have
• The words in order of importance: Dunmore Hale, Sauvignon Blanc, Marlborough, New Zealand. It should be fit to the bottle posted in the links
Nice to have
• a pill shape or circular shape
Should not have
• Illustrations of wine bottles, wine glasses, or grapes

```html
<!DOCTYPE html>
<html lang="en">
<head>
<meta charset="utf-8">
<title>Dunmore Hale — Sauvignon Blanc Label</title>
<link href="https://fonts.googleapis.com/css2?family=Cinzel:wght@400;600&display=swap" rel="stylesheet">
<style>
  :root {
    --backdrop: #0b0b0c;
    --label-navy: #262a38;
    --label-navy-deep: #1c1f2a;
    --rim-gold: #e4e6a0;
    --rim-green: #b7c64a;
    --accent-green: #9cc24a;
    --ink-dark: #111318;
    --text-muted: #3a3e4c;
  }
  * { margin: 0; padding: 0; box-sizing: border-box; }
  html, body {
    width: 1200px;
    height: 1200px;
    overflow: hidden;
    background: var(--backdrop);
  }
  .canvas {
    position: relative;
    width: 1200px;
    height: 1200px;
    display: flex;
    align-items: center;
    justify-content: center;
  }
  .front-label {
    position: relative;
    width: 600px;
    height: 880px;
    border-radius: 300px / 330px;
    background: linear-gradient(90deg, var(--rim-green), var(--rim-gold) 50%, var(--rim-green));
    padding: 16px;
  }
  .front-label__face {
    width: 100%;
    height: 100%;
    border-radius: 284px / 314px;
    background: radial-gradient(ellipse at 50% 40%, var(--label-navy) 0%, var(--label-navy-deep) 100%);
    display: flex;
    flex-direction: column;
    align-items: center;
    padding-top: 70px;
    font-family: "Cinzel", serif;
    text-align: center;
  }
  .crest-ornament {
    width: 90px;
    height: 100px;
    border-radius: 45px 45px 20px 20px;
    background: linear-gradient(180deg, #a9cf55, #7ea23a);
  }
  .brand-name {
    margin-top: 40px;
    font-size: 92px;
    font-weight: 600;
    line-height: 0.95;
    color: var(--ink-dark);
    letter-spacing: -1px;
  }
  .vineyard-scene {
    margin-top: 46px;
    width: 230px;
    height: 150px;
    border-radius: 12px;
    background: linear-gradient(180deg, #8fb848, #6e9430);
  }
  .varietal {
    margin-top: 56px;
    font-size: 40px;
    font-weight: 400;
    color: var(--ink-dark);
    letter-spacing: 1px;
  }
  .vintage {
    font-size: 30px;
    color: var(--ink-dark);
    margin-top: 4px;
  }
  .region {
    margin-top: 40px;
    font-size: 30px;
    color: var(--ink-dark);
  }
  .country {
    font-size: 15px;
    letter-spacing: 2px;
    color: var(--ink-dark);
  }
</style>
</head>
<body>
  <main class="canvas">
    <section class="front-label">
      <div class="front-label__face">
        <div class="crest-ornament" role="img" aria-label="Green fleur-de-lis crest ornament"></div>
        <h1 class="brand-name">Dunmore<br>Hale</h1>
        <div class="vineyard-scene" role="img" aria-label="Green line illustration of a chateau above rolling vineyard rows"></div>
        <p class="varietal">SAUVIGNON BLANC</p>
        <p class="vintage">2023</p>
        <p class="region">MARLBOROUGH</p>
        <p class="country">NEW ZEALAND</p>
      </div>
    </section>
  </main>
</body>
</html>
```